Panel Forge App redesign proposal

Proposal for redesign of the main screens of our comic book creation app Panel Forge which is currently available for iPhone and iPad on App Store here:

https://apps.quillmarket.example/us/app/panel-forge/id907214563?mt=8

We are looking for suggestions for a new modern, polished and professional look for Panel Forge. The focus should be on icons, colors, and fonts on the main editing screen.

This project is not a full redesign, but should merely contain suggestions for what the app could look like!

Proposals are preferably based on the current design/layout of the app's components, and should focus on redesign of icons or colors.

Proposals should be based on the screenshots on App Store (attached). I.e. preferably replacing them with the new look of the app. Proposals are required in both iPhone 6 and iPad (Air/Mini) screen sizes (Retina).

The new look should be:
• Professional and clean
• Stay somewhat in line with iOS guidelines
• Mostly flat design
• Quiet (not dominate users' content)
• Exciting but not too playful
• Accessible and easy to navigate (no ambiguous icons or gestures. Labels on tool buttons).
• Use only fonts on iOS7 or higher

Preferably, most or all 10 attached screenshots should be replaced with your proposed counterparts reusing the current user content ("Garden Goblin" and "On the hill") . I.e. replace fonts, colors, and icons only. You are free to create your own screenshots from scratch, if you feel that can better reflect your proposal.

We can provide free access to the app using promotional codes.

We are interested in redesigning the app, so if we see a good proposal we will be interested in further collaboration

About the app
------------------------------------------
Panel Forge is a comic book creation app for iOS (iPad and iPhone) purchased and downloaded by many hundreds of thousands of users.

The app has been around since 2009 with several major updates and is one of the first and best comic book creation apps for iOS.

It is a very feature rich app. Its features include:
• page design with many photos
• books with multiple pages
• many balloon options (head and tail settings)
• merge of balloons and adding tail control points for better tail control
• complex text layout (warp and perspective)
• easy in-app font installation from font websites
• stickers (built-in and ability to add)
• built-in drawing
• image filters
• image blending modes and opacity
• built-in Dropbox file support
• PDF support (both import and export)
• layer management
and much, much more.

Please contact us if you would like promotional code to test the app.
Updates

Reason: Haven't received satisfactory suggestions. At least a number of both iPhone and iPad screenshots are needed.

Target Market(s)

Children, parents, and hobby comic book creators.

Requirements
Must have
• Replace at least 6 screenshots with your own proposal.
Nice to have
• • Professional, clean, simple
• • Stay somewhat in line with iOS guidelines
• • Mostly flat design
• • Quiet (not dominate users' content)
• • Accessible and easy to navigate (no ambiguous icons or gestures)
Should not have
• • Not too many items on screen
• • Not ambiguous
• • Not too colorful/playful

```html
<!DOCTYPE html>
<html lang="en">
<head>
<meta charset="utf-8">
<title>Panel Forge – Text Effect Editor</title>
<link rel="stylesheet" href="https://fonts.googleapis.com/css2?family=Bangers&family=Inter:wght@400;500;600&family=Comic+Neue:wght@700&family=Caveat+Brush&family=Anton&family=Kalam:wght@700&display=swap">
<style>
  :root{
    --screen-bg:#ffffff;
    --ink:#1b1b1b;
    --muted:#8a8a8a;
    --divider:#e6e6e6;
    --title-top:#ff2f86;
    --title-bottom:#ff9a1f;
    --sticker-pink:#f2558f;
    --gold-top:#f2c34a;
    --gold-bottom:#a8721c;
    --sky-top:#1a78ff;
    --sky-bottom:#33d6f0;
    --burst-red:#d8232a;
  }
  *{box-sizing:border-box;margin:0;padding:0}
  html,body{width:732px;height:1200px;overflow:hidden;background:var(--screen-bg)}
  .screen{position:relative;width:732px;height:1200px;background:var(--screen-bg);font-family:"Inter",sans-serif;color:var(--ink)}

  /* status bar */
  .status-bar{position:absolute;top:0;left:0;right:0;height:40px;display:flex;align-items:center;justify-content:space-between;padding:0 24px;font-size:20px}
  .status-left{display:flex;align-items:center;gap:8px}
  .signal{letter-spacing:-2px;font-size:14px}
  .status-time{position:absolute;left:0;right:0;text-align:center;font-weight:500;pointer-events:none}
  .status-right{display:flex;align-items:center;gap:8px}
  .battery{width:40px;height:17px;border:1.5px solid var(--ink);border-radius:3px;padding:2px;position:relative}
  .battery::before{content:"";display:block;width:100%;height:100%;background:var(--ink);border-radius:1px}
  .battery::after{content:"";position:absolute;right:-5px;top:4px;width:3px;height:6px;background:var(--ink);border-radius:0 2px 2px 0}

  /* comic page */
  .page{position:absolute;top:0;left:0;width:732px;height:800px}
  .cell{position:absolute;overflow:hidden}
  .cell-skate{left:11px;top:132px;width:349px;height:215px;background:linear-gradient(180deg,#9fb7c9 0%,#6f8a5a 38%,#a7a49a 62%,#c9c2b4 100%)}
  .cell-friends{left:370px;top:132px;width:350px;height:215px;background:linear-gradient(135deg,#5f9c8a 0%,#c9a27c 45%,#8b5a44 75%,#3e2a25 100%)}
  .cell-selfie{left:11px;top:355px;width:709px;height:435px;background:linear-gradient(170deg,#e8ecef 0%,#c9d3c8 30%,#b48a6a 55%,#6e4a36 80%,#3b2c28 100%)}

  .page-title{position:absolute;left:0;right:0;top:52px;text-align:center;font-family:"Bangers",sans-serif;font-size:112px;line-height:1;letter-spacing:2px;transform:skewX(-8deg);background:linear-gradient(180deg,var(--title-top) 0%,var(--title-top) 40%,var(--title-bottom) 100%);-webkit-background-clip:text;background-clip:text;color:transparent;filter:drop-shadow(0 3px 0 #fff)}

  .balloon{position:absolute}
  .balloon-text{position:absolute;inset:0;display:flex;align-items:center;justify-content:center;font-family:"Comic Neue",sans-serif;font-weight:700;color:#111}
  .balloon-jenny{left:168px;top:207px;width:132px;height:58px}
  .balloon-jenny .balloon-text{font-size:11px;height:40px}
  .balloon-bad{left:305px;top:392px;width:150px;height:100px}
  .balloon-bad .balloon-text{font-size:22px;height:66px}

  .sound-poof{position:absolute;left:538px;top:273px;font-family:"Bangers",sans-serif;font-size:34px;color:#fff;transform:rotate(-14deg);-webkit-text-stroke:1.5px #111;letter-spacing:1px}

  /* sticker picker */
  .picker{position:absolute;left:0;right:0;top:810px;height:250px}
  .picker-row{position:absolute;left:0;right:0;height:90px}
  .picker-row:nth-child(1){top:10px}
  .picker-row:nth-child(2){top:135px}
  .effect{position:absolute;top:0;width:130px;height:90px;margin-left:-65px;display:flex;flex-direction:column;align-items:center;justify-content:center;text-align:center;line-height:.95}
  .e1{left:93px}.e2{left:247px}.e3{left:391px}.e4{left:531px}.e5{left:656px}
  .warped{font-family:"Bangers",sans-serif;font-size:32px;transform:skewX(-10deg) rotate(-6deg);background:linear-gradient(180deg,var(--title-top),var(--title-bottom));-webkit-background-clip:text;background-clip:text;color:transparent}
  .burst{width:110px;height:70px}
  .sticker-text{font-family:"Caveat Brush",sans-serif;font-size:34px;color:var(--sticker-pink);letter-spacing:1px}
  .old-gold{font-family:"Anton",sans-serif;font-size:30px;background:linear-gradient(180deg,var(--gold-top),var(--gold-bottom));-webkit-background-clip:text;background-clip:text;color:transparent}
  .sky-blue{font-family:"Kalam",cursive;font-size:32px;font-style:italic;background:linear-gradient(180deg,var(--sky-top),var(--sky-bottom));-webkit-background-clip:text;background-clip:text;color:transparent}

  /* tab bar */
  .tab-bar{position:absolute;left:0;right:0;bottom:0;height:117px;border-top:1px solid var(--divider);display:flex}
  .tab{position:absolute;top:22px;width:120px;margin-left:-60px;display:flex;flex-direction:column;align-items:center;gap:14px;font-size:13px;letter-spacing:.5px;color:var(--muted)}
  .tab svg{width:44px;height:44px}
  .t1{left:76px}.t2{left:213px}.t3{left:360px}.t4{left:509px}.t5{left:643px}
  .tab-aa{font-size:38px;line-height:44px;height:44px;color:#8d8d8d;font-weight:500}
</style>
</head>
<body>
<main class="screen">

  <header class="status-bar">
    <div class="status-left">
      <span class="signal">●●●○○</span><span>CREST</span>
      <svg width="22" height="16" viewBox="0 0 22 16" aria-hidden="true"><path d="M2 6a13 13 0 0 1 18 0M5 9.5a8.5 8.5 0 0 1 12 0M8 13a4 4 0 0 1 6 0" fill="none" stroke="#1b1b1b" stroke-width="2" stroke-linecap="round"/></svg>
    </div>
    <span class="status-time">4:21 PM</span>
    <div class="status-right">
      <svg width="12" height="20" viewBox="0 0 12 20" aria-hidden="true"><path d="M1 5l10 9-5 4V2l5 4L1 15" fill="none" stroke="#9a9a9a" stroke-width="1.6"/></svg>
      <span>100%</span><span class="battery"></span>
    </div>
  </header>

  <section class="page">
    <div class="cell cell-skate" role="img" aria-label="Photo: a girl on a skateboard pushed by a friend in a park"></div>
    <div class="cell cell-friends" role="img" aria-label="Photo: three friends in sunglasses lying close together"></div>
    <div class="cell cell-selfie" role="img" aria-label="Photo: three friends taking a selfie outdoors"></div>

    <h1 class="page-title">DAY OF JOY</h1>

    <div class="balloon balloon-jenny">
      <svg width="132" height="58" viewBox="0 0 132 58" aria-hidden="true"><path d="M66 2C33 2 6 10 6 21s27 19 60 19c4 0 8 0 11-1L55 56l36-19c22-3 36-9 36-16C127 10 99 2 66 2z" fill="#fff" stroke="#111" stroke-width="2"/></svg>
      <span class="balloon-text">AHHH, NO JENNY!</span>
    </div>

    <span class="sound-poof">POOFFF</span>

    <div class="balloon balloon-bad">
      <svg width="150" height="100" viewBox="0 0 150 100" aria-hidden="true"><path d="M75 3C38 3 8 17 8 36s30 32 60 33l38 28-12-30c28-5 48-17 48-31C142 17 112 3 75 3z" fill="#fff" stroke="#111" stroke-width="2.5"/></svg>
      <span class="balloon-text">AINT BAD!</span>
    </div>
  </section>

  <section class="picker" aria-label="Text effects">
    <div class="picker-row">
      <div class="effect e1 warped"><span>WARPED</span><span>TEXT</span></div>
      <div class="effect e2"><div class="burst" role="img" aria-label="Red comic burst sticker" style="background:radial-gradient(ellipse at center,var(--burst-red) 0%,#b31a20 55%,rgba(255,255,255,0) 72%)"></div></div>
      <div class="effect e3 sticker-text"><span>Sticker</span><span>text</span></div>
      <div class="effect e4 old-gold"><span>Old</span><span>Gold</span></div>
      <div class="effect e5 sky-blue"><span>Sky</span><span>Blue</span></div>
    </div>
    <div class="picker-row">
      <div class="effect e1 warped"><span>WARPED</span><span>TEXT</span></div>
      <div class="effect e2"><div class="burst" role="img" aria-label="Red comic burst sticker" style="background:radial-gradient(ellipse at center,var(--burst-red) 0%,#b31a20 55%,rgba(255,255,255,0) 72%)"></div></div>
      <div class="effect e3 sticker-text"><span>Sticker</span><span>text</span></div>
      <div class="effect e4 old-gold"><span>Old</span><span>Gold</span></div>
      <div class="effect e5 sky-blue"><span>Sky</span><span>Blue</span></div>
    </div>
  </section>

  <nav class="tab-bar">
    <div class="tab t1">
      <svg viewBox="0 0 44 44" aria-hidden="true"><path d="M27 8L13 22l14 14" fill="none" stroke="#8d8d8d" stroke-width="2.5" stroke-linecap="round" stroke-linejoin="round"/></svg>
      <span>DONE</span>
    </div>
    <div class="tab t2">
      <svg viewBox="0 0 44 44" aria-hidden="true"><path d="M22 7C12 7 4 13 4 20c0 5 4 9 9 11l-3 7 9-6c1 0 2 0 3 0 10 0 18-5 18-12S32 7 22 7z" fill="none" stroke="#8d8d8d" stroke-width="2.2" stroke-linejoin="round"/></svg>
      <span>BALLOON</span>
    </div>
    <div class="tab t3">
      <svg viewBox="0 0 44 44" aria-hidden="true"><polygon points="22,4 25,12 32,7 31,15 40,14 34,21 41,26 32,28 35,36 27,32 22,40 18,32 10,36 12,28 3,26 10,21 4,14 13,15 12,7 19,12" fill="#8d8d8d"/></svg>
      <span>STICKER</span>
    </div>
    <div class="tab t4">
      <span class="tab-aa">Aa</span>
      <span>TEXT EFFECT</span>
    </div>
    <div class="tab t5">
      <svg viewBox="0 0 44 44" aria-hidden="true"><rect x="8" y="8" width="28" height="28" fill="none" stroke="#8d8d8d" stroke-width="1.5" stroke-dasharray="3 3"/><g fill="#fff" stroke="#8d8d8d" stroke-width="1.5"><rect x="5" y="5" width="6" height="6"/><rect x="33" y="5" width="6" height="6"/><rect x="5" y="33" width="6" height="6"/><rect x="33" y="33" width="6" height="6"/><rect x="19" y="5" width="6" height="6"/><rect x="19" y="33" width="6" height="6"/></g></svg>
      <span>CELL</span>
    </div>
  </nav>

</main>
</body>
</html>
```